Meridian Forum Flyer

We need a company flyer to present our company. Target group: Senior managers of hospitals / care facilities.
Please use the new text from the document "Kongressflyer.pptx".
Design: The last flyer can be used as a design basis - attached here: "Bright Orbit Flyer High Res Compressed.pdf". Please note the layout of the business card. The flyer must visually match the business card.
Logos for the references attached (KTW, Varmon, Chemnitz, Cologne, Am Lindenhain, Brückwerk, Tobe, PLMR).
Format: DIN A long in portrait format, front and back printed (or open to alternative suggestions if the format does not appear optimal from a design point of view)
Timing: We need the flyer as soon as possible

```html
<!DOCTYPE html>
<html lang="de">
<head>
<meta charset="utf-8">
<title>Meridian Forum Flyer</title>
<link href="https://fonts.googleapis.com/css2?family=Open+Sans:wght@400;600;700;800&display=swap" rel="stylesheet">
<style>
:root{
  --stage:#e4e6e8;
  --teal-dark:#0e4756;
  --teal:#1b95a1;
  --teal-light:#7fd3da;
  --red:#d0202e;
  --blue:#1b5d8c;
  --ink:#2d3a40;
  --paper:#ffffff;
  --line:#d8e0e3;
}
*{box-sizing:border-box;margin:0;padding:0}
html,body{width:753px;height:1200px;overflow:hidden}
body{background:var(--stage);font-family:"Open Sans",Arial,sans-serif;color:var(--ink);position:relative}
.flyer{position:absolute;top:228px;width:350px;height:744px;background:var(--paper);display:flex;flex-direction:column;box-shadow:0 4px 14px rgba(0,0,0,.18);overflow:hidden}
.flyer--front{left:18px}
.flyer--back{left:385px}
.header{height:86px;flex:none;background:var(--teal-dark);position:relative;display:flex;align-items:center;justify-content:space-between;padding:0 18px;overflow:hidden}
.header .wave{position:absolute;left:0;bottom:0}
.brand{position:relative;display:flex;align-items:center;gap:6px;color:#fff;font-weight:700;font-size:13px}
.brand .dot{width:14px;height:14px;border-radius:50%;background:var(--teal)}
.brand--main{font-size:22px;font-weight:800}
.body{flex:1;padding:14px 16px 8px;font-size:8.6px;line-height:1.45;overflow:hidden}
.lead{color:var(--red);font-weight:800;font-size:10.6px;line-height:1.32;margin-bottom:8px}
.lead--dark{color:var(--teal-dark)}
.sub{color:var(--blue);font-weight:700;font-size:8.8px;margin-bottom:8px}
.h{font-weight:800;font-size:10px;margin:10px 0 4px}
.h--red{color:var(--red)}
.h--dark{color:var(--teal-dark)}
p{margin-bottom:5px}
.checks{list-style:none}
.checks li{display:flex;gap:6px;margin-bottom:6px}
.checks svg{flex:none;margin-top:2px}
.checks b{color:var(--teal-dark)}
.refs{display:grid;grid-template-columns:repeat(4,1fr);gap:7px;margin-top:6px}
.ref{height:32px;border:1px solid var(--line);display:flex;align-items:center;justify-content:center;font-weight:700;font-size:8px;color:var(--teal-dark);text-align:center;padding:0 2px}
.footer{flex:none;background:var(--teal-dark);color:#fff;padding:9px 16px 11px;font-size:7.6px}
.footer .title{color:var(--teal-light);font-weight:800;font-size:8px;margin-bottom:6px}
.footer .row{display:flex;justify-content:space-between;align-items:center;white-space:nowrap}
.footer .item{display:flex;align-items:center;gap:4px}
.pos{list-style:none;margin-bottom:4px}
.pos li{padding-left:9px;position:relative;margin-bottom:3px}
.pos li::before{content:"";position:absolute;left:0;top:4px;width:5px;height:5px;background:var(--teal)}
.call{color:var(--red);font-weight:800;font-size:10px;margin-top:12px}
.office{display:flex;gap:12px;margin-top:12px;align-items:center}
.photo{width:84px;height:84px;background:linear-gradient(160deg,#c9d3d8,#8d9ca4);flex:none}
.office .city{color:var(--teal-dark);font-weight:800;font-size:10px;margin-bottom:2px}
.office .name{font-weight:700;color:var(--blue)}
</style>
</head>
<body>

<section class="flyer flyer--front">
  <header class="header">
    <svg class="wave" width="350" height="86" viewBox="0 0 350 86"><path d="M0 70 Q120 40 350 62 L350 86 L0 86Z" fill="#1b95a1" opacity=".35"/></svg>
    <div class="brand"><span class="dot"></span>Lumen Health</div>
    <div class="brand brand--main">Harwell.</div>
  </header>
  <div class="body">
    <div class="lead">Sie sind Leiter eines Krankenhauses und suchen Medizinische Fachkräfte für Ihre Klinik oder Herausragende Führungskräfte für Ihre Klinikverwaltung?</div>
    <div class="sub">Wir finden für Sie die geeigneten Kandidaten schnell und zuverlässig. Wir unterstützen Sie gerne.</div>
    <div class="h h--dark">Wer sind wir?</div>
    <p>Seit fast 40 Jahren gehört das Unternehmen Harwell / Bright Orbit zu den führenden Personalberatungen im Gesundheitswesen. Die Besetzung von Spitzenpositionen für Kliniken ist unsere große Leidenschaft.</p>
    <p>Durch den Zusammenschluss der beiden Firmen haben wir uns breiter aufgestellt und sind heute moderner, digitaler und für die Zukunft gut aufgestellt – ohne dabei die Tradition aus dem Auge zu verlieren.</p>
    <div class="h h--red">Warum können wir Sie bestmöglich unterstützen?</div>
    <ul class="checks">
      <li><svg width="10" height="10" viewBox="0 0 10 10"><path d="M1 5 L4 8 L9 1" stroke="#1b95a1" stroke-width="2" fill="none"/></svg><span><b>Erfahrung:</b> Sie profitieren von Jahrzehnten an Wissen und passenden Kandidaten für Ihre Klinik.</span></li>
      <li><svg width="10" height="10" viewBox="0 0 10 10"><path d="M1 5 L4 8 L9 1" stroke="#1b95a1" stroke-width="2" fill="none"/></svg><span><b>Effizienz:</b> Wir arbeiten schnell, strukturiert und mit klaren Zielen für Sie.</span></li>
      <li><svg width="10" height="10" viewBox="0 0 10 10"><path d="M1 5 L4 8 L9 1" stroke="#1b95a1" stroke-width="2" fill="none"/></svg><span><b>Wir sind Spezialisten im Gesundheitswesen:</b> Unser Team kennt die Branche genau.</span></li>
      <li><svg width="10" height="10" viewBox="0 0 10 10"><path d="M1 5 L4 8 L9 1" stroke="#1b95a1" stroke-width="2" fill="none"/></svg><span><b>Überragendes Netzwerk:</b> In allen Sektoren des Gesundheitswesens.</span></li>
      <li><svg width="10" height="10" viewBox="0 0 10 10"><path d="M1 5 L4 8 L9 1" stroke="#1b95a1" stroke-width="2" fill="none"/></svg><span><b>Digital:</b> Unser Prozess ist transparent und modern für Sie.</span></li>
    </ul>
    <div class="h h--red">REFERENZEN</div>
    <div class="refs">
      <div class="ref">KTW</div><div class="ref">Varmon</div><div class="ref">Nordau</div><div class="ref">Rheinhof</div>
      <div class="ref">Am Lindenhain</div><div class="ref">Brückwerk</div><div class="ref">Tobe</div><div class="ref">PLMR</div>
    </div>
  </div>
  <footer class="footer">
    <div class="title">KONTAKTIEREN SIE UNS</div>
    <div class="row">
      <span class="item"><svg width="9" height="9" viewBox="0 0 10 10"><path d="M2 1 L4 1 L5 3 L4 4 Q5 6 6 6 L7 5 L9 6 L9 8 Q5 9 1 3Z" fill="#7fd3da"/></svg>+49 40 555 0142</span>
      <span>www.brightorbit.de</span>
      <span>www.beratung-harwell.de</span>
    </div>
  </footer>
</section>

<section class="flyer flyer--back">
  <header class="header">
    <svg class="wave" width="350" height="86" viewBox="0 0 350 86"><path d="M0 70 Q120 40 350 62 L350 86 L0 86Z" fill="#1b95a1" opacity=".35"/></svg>
    <div class="brand"><span class="dot"></span>Lumen Health</div>
    <div class="brand brand--main">Harwell.</div>
  </header>
  <div class="body">
    <div class="lead lead--dark">Was sind typische Positionen, die wir besetzen?</div>
    <div class="h h--red">Medizinische Fachkräfte</div>
    <p>Wir besetzen vor allem Führungspositionen in Kliniken aller Fachrichtungen, z. B.:</p>
    <ul class="pos">
      <li>Chefarzt Kardiologie / Gefäßmedizin</li>
      <li>Chefarzt Radiologie</li>
      <li>Chefarzt Psychiatrie</li>
    </ul>
    <div class="h h--red">Herausragende Führungskräfte</div>
    <p>Für die Verwaltung und das Management von Krankenhäusern und Pflegeeinrichtungen, z. B.:</p>
    <ul class="pos">
      <li>Geschäftsführung / Vorstand</li>
      <li>Leitung Personal</li>
      <li>Leitung Finanzen und Controlling</li>
      <li>Leitung Qualitäts- und Risikomanagement</li>
      <li>Leitung Pflegedirektion</li>
    </ul>
    <div class="call">WIR FREUEN UNS, VON IHNEN ZU HÖREN!</div>
    <div class="office">
      <div class="photo" role="img" aria-label="Porträtfoto der Ansprechpartnerin Büro Hamburg"></div>
      <div><div class="city">BÜRO HAMBURG</div><div class="name">Dr. Jana Roth</div><div>+49 40 555 0142</div><div>roth@brightorbit.de</div></div>
    </div>
    <div class="office">
      <div class="photo" role="img" aria-label="Porträtfoto des Ansprechpartners Büro Wien"></div>
      <div><div class="city">BÜRO WIEN</div><div class="name">Lukas Berger</div><div>+43 1 555 0198</div><div>berger@brightorbit.de</div></div>
    </div>
    <div class="office">
      <div class="photo" role="img" aria-label="Porträtfoto der Ansprechpartnerin Büro Düsseldorf"></div>
      <div><div class="city">BÜRO DÜSSELDORF</div><div class="name">Miriam Falk</div><div>+49 211 555 0176</div><div>falk@brightorbit.de</div></div>
    </div>
  </div>
  <footer class="footer">
    <div class="title">KONTAKTIEREN SIE UNS</div>
    <div class="row">
      <span class="item"><svg width="9" height="9" viewBox="0 0 10 10"><path d="M2 1 L4 1 L5 3 L4 4 Q5 6 6 6 L7 5 L9 6 L9 8 Q5 9 1 3Z" fill="#7fd3da"/></svg>+49 40 555 0142</span>
      <span>www.brightorbit.de</span>
      <span>www.beratung-harwell.de</span>
    </div>
  </footer>
</section>

</body>
</html>
```